Crestline Gas and Plumbing Business Card Design

I am after a business card design for my plumbing business called 'Crestline Gas & Plumbing'. I do all types of plumbing and gas work and specialise in general maintenance plumbing. Would like to see designs using current logo

Industry/Entity Type

Plumbing

Contact Information for Business Card

Name - Dale Whitcombe
Phone number - 0455163027
Email - admin@crestlinegasandplumbing.example.com.au
ABN - 68204915336

```html
<!DOCTYPE html>
<html lang="en">
<head>
<meta charset="utf-8">
<title>Crestline Gas &amp; Plumbing – Business Card</title>
<link href="https://fonts.googleapis.com/css2?family=Cinzel:wght@700&family=Arimo:wght@400&display=swap" rel="stylesheet">
<style>
  :root {
    --backdrop: #2a2a2a;
    --card-white: #ffffff;
    --brand-blue: #4561fb;
    --deep-blue: #2b4fe0;
    --brand-orange: #fdb01e;
    --name-blue: #1f5fc4;
    --accent-orange: #f5a623;
  }
  * { margin: 0; padding: 0; box-sizing: border-box; }
  html, body {
    width: 994px; height: 1200px; overflow: hidden;
    background: var(--backdrop);
  }
  .canvas { position: relative; width: 994px; height: 1200px; }
  .card {
    position: absolute; left: 67px;
    width: 843px; height: 482px;
    background: var(--card-white);
    overflow: hidden;
  }
  .card--front { top: 67px; }
  .card--back { top: 625px; }

  .decor-area {
    position: absolute; top: 0; height: 100%;
    background: linear-gradient(160deg, var(--brand-orange) 0%, var(--deep-blue) 45%, var(--brand-blue) 100%);
  }
  .card--front .decor-area { right: 0; width: 230px; }
  .card--back .decor-area { left: 0; width: 220px;
    background: linear-gradient(200deg, var(--brand-orange) 0%, var(--deep-blue) 45%, var(--brand-blue) 100%); }
  .footer-band {
    position: absolute; left: 0; bottom: 0; width: 520px; height: 72px;
    background: var(--brand-blue);
  }

  .wordmark {
    position: absolute; display: flex; align-items: center; gap: 14px;
    font-family: "Cinzel", serif; font-weight: 700; color: var(--name-blue);
    transform: translate(-50%, -50%);
  }
  .wordmark-dot { width: 46px; height: 46px; border-radius: 50%; background: var(--brand-orange); flex: none; }
  .wordmark-name { display: flex; flex-direction: column; align-items: center; line-height: 1; }
  .wordmark-main { font-size: 44px; letter-spacing: 1px; }
  .wordmark-sub { font-size: 17px; letter-spacing: 3px; margin-top: 6px; }
  .card--front .wordmark { left: 343px; top: 228px; }
  .card--back .wordmark { left: 478px; top: 128px; }
  .card--back .wordmark-main { font-size: 32px; }
  .card--back .wordmark-sub { font-size: 13px; letter-spacing: 2px; }
  .card--back .wordmark-dot { width: 36px; height: 36px; }

  .abn {
    position: absolute; right: 33px; top: 442px;
    font-family: "Arimo", sans-serif; font-weight: 400; font-size: 15px;
    color: var(--card-white); letter-spacing: 0.5px;
  }
  .contact-name, .contact-phone {
    position: absolute; left: 478px; transform: translateX(-50%);
    white-space: nowrap; font-family: "Cinzel", serif; font-weight: 700;
  }
  .contact-name { top: 216px; font-size: 33px; color: var(--name-blue); }
  .contact-phone { top: 262px; font-size: 27px; color: var(--accent-orange); }
  .contact-email {
    position: absolute; left: 30px; top: 434px;
    font-family: "Arimo", sans-serif; font-size: 19px; color: var(--card-white);
    white-space: nowrap;
  }
</style>
</head>
<body>
<main class="canvas">

  <section class="card card--front" aria-label="Card front">
    <div class="decor-area" role="img" aria-label="Decorative blue and orange wave area"></div>
    <div class="wordmark">
      <span class="wordmark-dot"></span>
      <span class="wordmark-name"><span class="wordmark-main">CRESTLINE</span><span class="wordmark-sub">GAS &amp; PLUMBING</span></span>
    </div>
    <p class="abn">ABN - 68204915336</p>
  </section>

  <section class="card card--back" aria-label="Card back">
    <div class="decor-area" role="img" aria-label="Decorative blue and orange wave area"></div>
    <div class="footer-band"></div>
    <div class="wordmark">
      <span class="wordmark-dot"></span>
      <span class="wordmark-name"><span class="wordmark-main">CRESTLINE</span><span class="wordmark-sub">GAS &amp; PLUMBING</span></span>
    </div>
    <p class="contact-name">Dale Whitcombe</p>
    <p class="contact-phone">Phone No - 0455163027</p>
    <p class="contact-email">admin@crestlinegasandplumbing.example.com.au</p>
  </section>

</main>
</body>
</html>
```